Dynamic Business Card for Sports Supplements Company

Hi! I'm looking for an awesome business card to match my existing sports supplement company. I have uploaded my current company logo and screenshot of the front page of my website.

I would like to have something dynamic and interesting and utilize the colors in the website - the reds and purples

The business card should be double sided and focus on a unique eye-catching design on the back and include all the relevant company info.

Most importantly, it should say somewhere: "Sign up on our website for a coupon code."

Target Market(s)

Mostly for women gym goers but it shouldn't be too feminine. It should be in keeping with the website design. It should flow and clearly be connected to it

Industry/Entity Type

Business

Contact Information for Business Card

Colleen M. Varga
CEO
CVarga@Vitalorexco.example
www.vitalorexco.example
555.014.3827
P.O. Box 48317
Burke, Virginia 00000

Sign up on our website for a coupon code

Font styles to use
Serif
Sans Serif
Other font styles liked:
• Novecento font family and "Vitalorex" is in AR Destine font

Requirements
Must have
• One side should be a bold Vitalorex logo design. Even just the symbol itself may be o.k. (see attached file)

```html
<!DOCTYPE html>
<html lang="en">
<head>
<meta charset="utf-8">
<title>Vitalorex Business Card</title>
<link rel="stylesheet" href="https://fonts.googleapis.com/css2?family=Arimo:wght@400;700&display=swap">
<style>
  :root{
    --bg:#e9e7e4;
    --card:#141414;
    --card-edge:#1d1d1d;
    --ink:#f2f2f2;
    --ink-soft:#9a9a9a;
    --emboss:#3b3b3b;
    --accent:#d8232a;
    --rule:#cfcfcf;
  }
  *{margin:0;padding:0;box-sizing:border-box}
  html,body{width:1200px;height:864px;overflow:hidden;background:var(--bg)}
  body{position:relative;font-family:"Arimo",Arial,sans-serif}
  .card{
    position:absolute;width:600px;height:343px;
    background:linear-gradient(135deg,var(--card-edge),var(--card));
    border-radius:4px;box-shadow:0 10px 24px rgba(0,0,0,.28);
    overflow:hidden;
  }
  .card--back{left:60px;top:70px}
  .card--front{left:540px;top:450px}

  .brand-mark{position:absolute;display:flex;align-items:center;gap:12px}
  .brand-mark__square{width:30px;height:30px;flex:none}
  .brand-name{font-weight:700;letter-spacing:1px;line-height:1;white-space:nowrap}
  .tagline{position:absolute;text-transform:uppercase;white-space:nowrap}

  /* back side */
  .card--back .brand-mark{left:90px;top:112px}
  .card--back .brand-mark__square{width:34px;height:34px;background:var(--emboss)}
  .card--back .brand-name{color:var(--emboss);font-size:44px}
  .card--back .tagline{left:136px;top:162px;color:var(--emboss);font-size:11px;letter-spacing:3px}
  .coupon-note{position:absolute;left:90px;top:200px;font-size:14px;color:var(--ink-soft)}

  /* front side */
  .contact{position:absolute;left:36px;top:116px}
  .contact__name{color:var(--accent);font-size:21px;line-height:24px}
  .contact__role{color:var(--ink);font-size:14px;margin-top:4px}
  .contact__list{list-style:none;margin-top:10px}
  .contact__item{display:flex;align-items:center;gap:9px;color:var(--ink);font-size:13px;height:22px}
  .contact__icon{width:12px;height:12px;flex:none}
  .rule{position:absolute;left:0;top:252px;width:568px;height:1px;background:var(--rule)}
  .card--front .brand-mark{left:344px;top:134px}
  .card--front .brand-mark__square{background:var(--accent)}
  .card--front .brand-name{color:var(--ink);font-size:32px}
  .card--front .tagline{left:386px;top:174px;color:var(--ink-soft);font-size:9px;letter-spacing:2.6px}
  .address{position:absolute;right:32px;top:270px;text-align:right;color:var(--ink);font-size:14px;line-height:20px;font-style:normal}
</style>
</head>
<body>

<section class="card card--back" aria-label="Card back">
  <div class="brand-mark">
    <span class="brand-mark__square"></span>
    <span class="brand-name">VITALOREX</span>
  </div>
  <p class="tagline">Built for every rep</p>
  <p class="coupon-note">Sign up on our website for a coupon code</p>
</section>

<section class="card card--front" aria-label="Card front">
  <div class="contact">
    <p class="contact__name">Colleen M. Varga</p>
    <p class="contact__role">CEO</p>
    <ul class="contact__list">
      <li class="contact__item">
        <svg class="contact__icon" viewBox="0 0 12 12"><path fill="#d8232a" d="M2.2 0.8l2 0 .8 2.6-1.3 1a6.5 6.5 0 0 0 2.9 2.9l1-1.3 2.6.8v2a1.2 1.2 0 0 1-1.3 1.2A9.6 9.6 0 0 1 1 2.1 1.2 1.2 0 0 1 2.2.8z"/></svg>
        555.014.3827
      </li>
      <li class="contact__item">
        <svg class="contact__icon" viewBox="0 0 12 12"><rect x="0.5" y="2" width="11" height="8" rx="1" fill="#d8232a"/><path d="M1 2.5l5 4 5-4" stroke="#141414" stroke-width="1" fill="none"/></svg>
        CVarga@Vitalorexco.example
      </li>
      <li class="contact__item">
        <svg class="contact__icon" viewBox="0 0 12 12"><circle cx="6" cy="6" r="5.5" fill="#d8232a"/><path d="M0.5 6h11M6 .5c-2.4 2.8-2.4 8.2 0 11M6 .5c2.4 2.8 2.4 8.2 0 11" stroke="#141414" stroke-width=".8" fill="none"/></svg>
        www.vitalorexco.example
      </li>
    </ul>
  </div>

  <div class="brand-mark">
    <span class="brand-mark__square"></span>
    <span class="brand-name">VITALOREX</span>
  </div>
  <p class="tagline">Built for every rep</p>

  <span class="rule"></span>

  <address class="address">
    P.O. Box 48317<br>
    Alder Springs, Oregon 00000
  </address>
</section>

</body>
</html>
```